Quarvelon stickers design for our main topics (for example: agile and Kanban)

We are looking for sticker design, that will reflect our cooperate identity and can be used for the different topics in our company. We would like to start with our Agile Coaching Offers with a Kanban Sticker saying "stop starting, start finishing", A bad example can be find in the file upload ;)
Check out our homepage to get a feeling for the cooperate identity (www.quarvelon-beispiel.ch)

Target Market(s)

Customers and trainees from our trainings

Industry/Entity Type

Consulting

Colors
0355a3
fbed22

Requirements
Must have
• a cool design thats fits to our customer design
the 2 lines can be changed for future stickers ... like in the example "stop starting, start finishing" and "we show you how"
Nice to have
• -
Should not have
• -

```html
<!DOCTYPE html>
<html lang="en">
<head>
<meta charset="utf-8">
<title>Quarvelon Sticker – Stop Starting, Start Finishing</title>
<link rel="stylesheet" href="https://fonts.googleapis.com/css2?family=Montserrat:wght@600;700;800&display=swap">
<style>
  :root {
    --page-bg: #1a1a1a;
    --brand-yellow: #fbed22;
    --brand-blue: #0355a3;
    --frame-white: #ffffff;
  }
  html, body {
    margin: 0;
    padding: 0;
    width: 1200px;
    height: 1200px;
    overflow: hidden;
    background: var(--page-bg);
  }
  .sticker {
    display: block;
    width: 1200px;
    height: 1200px;
  }
  .sticker-card { fill: var(--brand-yellow); stroke: var(--frame-white); stroke-width: 19; }
  .tilted-frame { fill: none; stroke: var(--frame-white); stroke-width: 18; }
  .sticker-text {
    fill: var(--brand-blue);
    font-family: "Montserrat", sans-serif;
  }
  .lead-line { font-size: 50px; font-weight: 700; }
  .headline-small { font-size: 104px; font-weight: 700; }
  .headline-large { font-size: 196px; font-weight: 800; }
  .tagline { font-size: 50px; font-weight: 700; }
  .company-name { font-size: 28px; font-weight: 600; }
</style>
</head>
<body>
<svg class="sticker" viewBox="0 0 1932 1932" xmlns="http://www.w3.org/2000/svg">
  <defs>
    <clipPath id="card-area">
      <rect x="172" y="476" width="1640" height="929"/>
    </clipPath>
  </defs>

  <rect class="sticker-card" x="181.5" y="485.5" width="1621" height="910"/>

  <polygon class="tilted-frame" clip-path="url(#card-area)"
           points="306,496 1753,633 1677,1393 230,1248"/>

  <text class="sticker-text lead-line" x="391" y="707"
        textLength="337" lengthAdjust="spacingAndGlyphs">Stop Starting...</text>

  <text class="sticker-text headline-small" x="475" y="878"
        textLength="457" lengthAdjust="spacing">START</text>

  <text class="sticker-text headline-large" x="483" y="1040"
        textLength="1023" lengthAdjust="spacingAndGlyphs">FINISHING</text>

  <text class="sticker-text tagline" x="1118" y="1148"
        textLength="415" lengthAdjust="spacingAndGlyphs">We show you how</text>

  <text class="sticker-text company-name" x="1380" y="1197"
        textLength="270" lengthAdjust="spacing">QUARVELON AG</text>
</svg>
</body>
</html>
```